business cards for heating company

I need business cards for my heating air conditioning and chimney company located in upstate NY I would like for them to be colorful and catchy on heavy stock with preferably a glossy finish on front of card but the ability to write something on one half of the back with maybe some bullets on the other half of the back I also need to be able to change the name and title of employees on the card and also incorporate some of our current look and feel from our trucks and website I also want to be able to use this design or similar to have door hangers made lawn signs coffee mugs key chains etc. our website is Brindlecove.com

Target Market(s)

homeowners

Industry/Entity Type

Air Conditioning

Contact Information for Business Card

should have website brindlecove.com , phone number 585-437-9168 please look at website for ideas

Font styles to use
Sans Serif

Colors
ec1f27
3176b5
fbee3f

Requirements
Must have
• a complete look
Nice to have
• a discount offer like 10% military and first responders
• senior discount %5

```html
<!DOCTYPE html>
<html lang="en">
<head>
<meta charset="utf-8">
<title>Brindle Cove – Business Cards</title>
<link rel="stylesheet" href="https://fonts.googleapis.com/css2?family=Questrial&family=Oswald:wght@400;500;600&family=Roboto+Condensed:wght@500;700&family=Playfair+Display:wght@400&display=swap">
<style>
  :root {
    --stage: #1c1c1d;
    --red: #c42a4d;
    --blue: #1d5aa8;
    --ink: #232323;
    --charcoal: #2e2e30;
    --paper: #ffffff;
    --panel-light: #ececec;
    --panel-dark: #151516;
    --panel-dark-2: #2a2a2c;
    --pink: #d46a80;
    --muted: #d9d9d9;
  }
  * { box-sizing: border-box; margin: 0; padding: 0; }
  html, body { width: 1200px; height: 871px; overflow: hidden; }
  body { background: var(--stage); position: relative; font-family: "Oswald", sans-serif; }

  .card { position: absolute; overflow: hidden; box-shadow: 0 18px 40px rgba(0,0,0,.55); }

  /* Back of card */
  .card-back { left: 60px; top: 50px; width: 620px; height: 354px; display: flex; }
  .services { width: 38%; background: var(--panel-light); padding: 38px 0 0 30px; }
  .services h3 { font-family: "Roboto Condensed", sans-serif; font-weight: 700; color: var(--red); font-size: 19px; letter-spacing: 1px; margin-bottom: 8px; }
  .services ul { list-style: none; }
  .services li { font-family: "Roboto Condensed", sans-serif; font-weight: 700; color: #4a4a4a; font-size: 15.5px; letter-spacing: 1px; line-height: 28px; display: flex; align-items: center; gap: 8px; }
  .services svg { width: 11px; height: 11px; fill: var(--blue); flex: none; }
  .offer-side { flex: 1; background: linear-gradient(135deg, var(--panel-dark-2), var(--panel-dark) 60%); padding: 34px 0 0 40px; }
  .brand-back { font-family: "Questrial", sans-serif; font-size: 36px; color: var(--paper); letter-spacing: 1px; line-height: 1; }
  .tagline-back { font-family: "Questrial", sans-serif; font-size: 12px; color: var(--muted); letter-spacing: 1px; margin: 6px 0 0 40px; }
  .site { font-family: "Oswald", sans-serif; font-size: 17px; letter-spacing: 4px; color: var(--pink); margin-top: 6px; }
  .site .blue { color: #4d86d0; }
  .offer { display: flex; align-items: flex-end; gap: 8px; margin-top: 20px; }
  .offer + .offer { margin-top: 4px; }
  .offer .pct { font-family: "Playfair Display", serif; font-size: 46px; line-height: 1; color: var(--pink); }
  .offer .pct small { font-size: 22px; vertical-align: top; }
  .offer .txt { font-family: "Oswald", sans-serif; color: var(--muted); font-size: 14px; letter-spacing: 1px; line-height: 1.15; padding-bottom: 4px; }
  .offer .txt b { color: var(--pink); font-weight: 400; font-size: 18px; display: block; }

  /* Front of card */
  .card-front { left: 500px; top: 440px; width: 650px; height: 372px; background: var(--paper); }
  .brand-front { position: absolute; left: 48px; top: 120px; }
  .brand-front .name { font-family: "Questrial", sans-serif; font-size: 44px; color: var(--blue); letter-spacing: 1px; line-height: 1; }
  .brand-front .tagline { font-family: "Questrial", sans-serif; font-size: 15px; color: var(--ink); margin: 8px 0 0 30px; letter-spacing: .3px; }
  .divider { position: absolute; left: 382px; top: 60px; width: 3px; height: 190px; background: var(--blue); }
  .contact { position: absolute; left: 406px; top: 70px; }
  .contact .person { font-family: "Oswald", sans-serif; font-weight: 600; font-size: 32px; color: var(--ink); letter-spacing: 1.5px; line-height: 1.1; }
  .contact .title { font-family: "Roboto Condensed", sans-serif; font-weight: 700; font-size: 17px; color: var(--red); letter-spacing: 2px; margin-bottom: 6px; }
  .contact .line { display: flex; align-items: center; gap: 14px; font-family: "Oswald", sans-serif; font-weight: 500; font-size: 19px; color: var(--ink); letter-spacing: 1px; line-height: 32px; }
  .contact svg { width: 14px; height: 14px; fill: var(--red); flex: none; }
  .stripe { position: absolute; left: 0; bottom: 0; width: 100%; height: 56px; display: flex; }
  .stripe .red { width: 36%; background: var(--red); }
  .stripe .dark { width: 24%; background: var(--charcoal); border-left: 5px solid var(--paper); }
  .stripe .blue { flex: 1; background: var(--blue); border-left: 5px solid var(--paper); }
</style>
</head>
<body>
  <svg width="0" height="0" style="position:absolute">
    <defs>
      <symbol id="burst" viewBox="0 0 12 12"><polygon points="6,0 7.3,3.6 11.2,2.6 8.5,5.6 12,7.8 8,8 7.6,12 6,8.6 4.4,12 4,8 0,7.8 3.5,5.6 0.8,2.6 4.7,3.6"/></symbol>
    </defs>
  </svg>

  <section class="card card-back" aria-label="Card back">
    <div class="services">
      <h3>OUR SERVICES</h3>
      <ul>
        <li><svg><use href="#burst"/></svg>EMERGENCY SERVICE</li>
        <li><svg><use href="#burst"/></svg>COMMERCIAL HVAC</li>
        <li><svg><use href="#burst"/></svg>BOAT HEATING/COOLING</li>
        <li><svg><use href="#burst"/></svg>EXPERT TUNE UP</li>
        <li><svg><use href="#burst"/></svg>CHIMNEY SWEEP</li>
        <li><svg><use href="#burst"/></svg>CHIMNEY CLEANING</li>
        <li><svg><use href="#burst"/></svg>HOME DUCT CLEANING</li>
        <li><svg><use href="#burst"/></svg>HEATING SOLUTIONS</li>
        <li><svg><use href="#burst"/></svg>COOLING SOLUTIONS</li>
      </ul>
    </div>
    <div class="offer-side" role="img" aria-label="Dark textured panel with company name, website and discounts">
      <div class="brand-back">BRINDLE COVE</div>
      <div class="tagline-back">HEATING, COOLING &amp; CHIMNEY</div>
      <div class="site">BRINDLE<span class="blue">COVE</span>.COM</div>
      <div class="offer"><span class="pct">10<small>%</small></span><span class="txt"><b>OFF</b>FOR MILITARY AND FIRST RESPONDERS</span></div>
      <div class="offer"><span class="pct">5<small>%</small></span><span class="txt"><b>OFF</b>FOR SENIORS</span></div>
    </div>
  </section>

  <section class="card card-front" aria-label="Card front">
    <div class="brand-front">
      <div class="name">BRINDLE COVE</div>
      <div class="tagline">HEATING, COOLING &amp; CHIMNEY</div>
    </div>
    <div class="divider"></div>
    <div class="contact">
      <div class="person">Your Name</div>
      <div class="title">JOB TITLE</div>
      <div class="line"><svg viewBox="0 0 14 14"><path d="M7 0a5 5 0 0 0-5 5c0 3.6 5 9 5 9s5-5.4 5-9a5 5 0 0 0-5-5zm0 7a2 2 0 1 1 0-4 2 2 0 0 1 0 4z"/></svg>Address</div>
      <div class="line"><svg viewBox="0 0 14 14"><path d="M1 4c0-1.5 2.7-2.5 6-2.5S13 2.5 13 4v1.5h-3V4H4v1.5H1zM3 7h8l2 5H1z"/></svg>585-437-9168</div>
      <div class="line"><svg viewBox="0 0 14 14"><path d="M0 3h14v8H0zm1 1 6 4 6-4"/></svg>Email</div>
    </div>
    <div class="stripe"><div class="red"></div><div class="dark"></div><div class="blue"></div></div>
  </section>
</body>
</html>
```